Architectural firm needs a graphic representation of our Master Planning process

We need an image to convey our 3-phase, 8-step Master Planning process that we utilize when designing plans for schools K-12. What we currently use looks very outdated in both the design and color scheme. We'd like an EPS created that can be scaled without distortion. The files I've attached show the current graphic and an instruction sheet which also contains our colors.

```html
<!DOCTYPE html>
<html lang="en">
<head>
<meta charset="utf-8">
<title>Master Planning Process</title>
<link href="https://fonts.googleapis.com/css2?family=Orbitron:wght@500&family=PT+Sans:wght@700&display=swap" rel="stylesheet">
<style>
  :root {
    --crimson: #b0093a;
    --crimson-deep: #8e0830;
    --overlap: #5c0616;
    --sage: #5f7f5d;
    --slate: #6c6a70;
    --paper: #efefef;
    --ink: #111111;
    --white: #ffffff;
  }
  html, body {
    margin: 0;
    padding: 0;
    width: 1200px;
    height: 849px;
    overflow: hidden;
    background: var(--paper);
  }
  .poster {
    display: block;
    width: 1200px;
    height: 849px;
  }
  .poster-title {
    font-family: "Orbitron", sans-serif;
    font-weight: 500;
    font-size: 50px;
    fill: var(--crimson);
  }
  .partner-label {
    font-family: "PT Sans", sans-serif;
    font-weight: 700;
    font-size: 32px;
    fill: var(--white);
  }
  .school-label {
    font-family: "PT Sans", sans-serif;
    font-weight: 700;
    font-size: 62px;
    fill: var(--white);
  }
  .step-label {
    font-family: "PT Sans", sans-serif;
    font-weight: 700;
    font-size: 20px;
    fill: var(--ink);
    letter-spacing: 0.5px;
  }
  .phase-label {
    font-family: "PT Sans", sans-serif;
    font-weight: 700;
    font-size: 46px;
    fill: var(--ink);
  }
  .chevron { stroke: var(--ink); stroke-width: 3; stroke-linejoin: miter; }
  .chevron--step { fill: var(--sage); }
  .chevron--phase { fill: url(#phaseFade); }
  .footer-text {
    font-family: "PT Sans", sans-serif;
    font-weight: 700;
    font-size: 22px;
    fill: var(--white);
  }
  .logo-text {
    font-family: "PT Sans", sans-serif;
    font-weight: 700;
    font-size: 24px;
    fill: var(--white);
  }
</style>
</head>
<body>
<svg class="poster" viewBox="0 0 1200 849" xmlns="http://www.w3.org/2000/svg" role="img" aria-label="Master planning process diagram">
  <defs>
    <linearGradient id="phaseFade" x1="0" y1="0" x2="0" y2="1">
      <stop offset="0" stop-color="#5f7f5d"/>
      <stop offset="0.5" stop-color="#b0093a"/>
      <stop offset="1" stop-color="#6c6a70"/>
    </linearGradient>
    <clipPath id="schoolClip"><circle cx="600" cy="258" r="170"/></clipPath>
  </defs>

  <rect class="backdrop" x="0" y="0" width="1200" height="849" fill="var(--paper)"/>

  <text class="poster-title" x="32" y="72" textLength="1128" lengthAdjust="spacingAndGlyphs">MASTER PLANNING PROCESS</text>

  <g class="partners">
    <circle cx="312" cy="258" r="144" fill="var(--sage)"/>
    <circle cx="888" cy="258" r="142" fill="var(--slate)"/>
    <circle cx="600" cy="258" r="170" fill="var(--crimson)"/>
    <g clip-path="url(#schoolClip)">
      <circle cx="312" cy="258" r="144" fill="var(--overlap)"/>
      <circle cx="888" cy="258" r="142" fill="var(--overlap)"/>
    </g>
    <text class="partner-label" x="306" y="250" text-anchor="middle">ARCHITECTURAL</text>
    <text class="partner-label" x="306" y="287" text-anchor="middle">CONSULTANT</text>
    <text class="school-label" x="598" y="277" text-anchor="middle">SCHOOL</text>
    <text class="partner-label" x="893" y="250" text-anchor="middle">FUND RAISING</text>
    <text class="partner-label" x="893" y="287" text-anchor="middle">CONSULTANT</text>
  </g>

  <g class="process-band">
    <polygon class="chevron chevron--phase" points="0,450 84,450 164,602 84,754 0,754"/>
    <polygon class="chevron chevron--step" points="84,450 228,450 308,602 228,754 84,754 164,602"/>
    <polygon class="chevron chevron--step" points="228,450 374,450 454,602 374,754 228,754 308,602"/>
    <polygon class="chevron chevron--step" points="374,450 522,450 602,602 522,754 374,754 454,602"/>
    <polygon class="chevron chevron--step" points="522,450 672,450 752,602 672,754 522,754 602,602"/>
    <polygon class="chevron chevron--phase" points="672,450 824,450 904,602 824,754 672,754 752,602"/>
    <polygon class="chevron chevron--step" points="824,450 978,450 1058,602 978,754 824,754 904,602"/>
    <polygon class="chevron chevron--phase" points="978,450 1114,450 1200,602 1114,754 978,754 1058,602"/>

    <text class="phase-label" transform="translate(72,602) rotate(-90)" text-anchor="middle">VISIONING</text>

    <g class="step-label">
      <text transform="translate(196,532) rotate(90)" text-anchor="middle">PHYSICAL<tspan x="0" dy="22">CONDITIONS</tspan></text>
      <text transform="translate(206,680) rotate(90)" text-anchor="middle">ASESSMENT</text>

      <text transform="translate(334,532) rotate(90)" text-anchor="middle">SPACE NEEDS</text>
      <text transform="translate(346,680) rotate(90)" text-anchor="middle">ASESSMENT</text>

      <text transform="translate(482,530) rotate(90)" text-anchor="middle">PROBLEM</text>
      <text transform="translate(498,668) rotate(90)" text-anchor="middle">DEFINED</text>

      <text transform="translate(642,536) rotate(90)" text-anchor="middle">IDENTIFY</text>
      <text transform="translate(634,680) rotate(90)" text-anchor="middle">SOLUTIONS</text>

      <text transform="translate(794,596) rotate(90)" text-anchor="middle">ASSESS &amp; SELECT</text>

      <text transform="translate(942,540) rotate(90)" text-anchor="middle">COMPILE</text>
      <text transform="translate(950,656) rotate(90)" text-anchor="middle">REPORT</text>

      <text transform="translate(1086,532) rotate(90)" text-anchor="middle">IMPLEMENT</text>
      <text transform="translate(1098,652) rotate(90)" text-anchor="middle">PLAN!</text>
    </g>
  </g>

  <g class="footer">
    <rect x="0" y="796" width="1200" height="53" fill="var(--slate)"/>
    <rect x="29" y="796" width="1142" height="53" fill="var(--crimson)"/>
    <rect x="29" y="796" width="14" height="53" fill="var(--crimson-deep)"/>
    <rect x="1157" y="796" width="14" height="53" fill="var(--crimson-deep)"/>
    <text class="footer-text" x="110" y="829">www.harborline.com</text>
    <text class="footer-text" x="1088" y="829" text-anchor="end">info@harborline.com</text>
    <circle cx="600" cy="806" r="36" fill="var(--slate)"/>
    <text class="logo-text" x="600" y="814" text-anchor="middle">Logo</text>
  </g>
</svg>
</body>
</html>
```